Home and interior page website design for HVAC company - Velmor Corp.

Create homepage and one interior page website design for an HVAC (Heating and AC) company. Current website is: https://velmorcorp.example/.

Client has specifically asked that the new site look inviting, informative and interactive. They mentioned that the logo on a white background doesn't look appealing and would like to see other options. (I have included the white background one from their current website as well as the one on an image that the client sent me) The site must include their financing widget (we have the code for this) in a prominent place. Image can be found here: https://getlendquick.example/badges/lendquick-financing.png.

The content from their existing site belongs to the company that built their site and have said we cannot use any of it. This development site (http://velmorwebd.qrbdev.example/) is what we originally created from our template for them before they decided they wanted a custom built site. The content there is what will need to be on the new home page.

We have gathered images from the client that they would like used throughout the site in this folder: https://climbrisk-my.filebox.example/:f:/g/personal/officelogin_climbrisk_filebox_example/Xq2m-R7TpLoWnZbYuCdE5FgHjK8NvA3sQwErTyUiOpLk?e=7KPZRT. They would like the photos used to be in tune with the topic being spoken about so if the topic is maintenance on a central AC system the photo used to lead that topic should be of a unit being cleaned.

For the testimonials section please also include a button or "Click here for more testimonials" as requested by the client.

Top Level NAV should include: Home, Residential, Commercial, Testimonials, Gallery, About Us, Coupons, Contact Us

For the interior page, we're looking for the same inviting, informative and interactive feel to the site, preferably with a banner of some sort and the form close to the top of the page if not able to keep it above the fold in the banner. Page should also include sections with clients images used to avoid a wall of text.

Example Websites that the client likes:
https://www.brelkordairworks.example/
https://www.quellitemp.example/?ref=PzR8vLm2KqT4nW9sXe6YuJ3aBc
https://www.torvandclimate.example/nny/
https://www.wexlo.example/
https://otterbrookheat.example/

Industry/Entity Type

Hvac

Number of Pages Required

2 page

Requirements
Must have
• *Summarized from project description:
-financing image in prominent place
-content from development site
-images from clients folder
-button or "click here.." note in testimonials section
-form above the fold
Nice to have
-logo not on white background

```html
<!DOCTYPE html>
<html lang="en">
<head>
<meta charset="utf-8">
<title>Velmor Corp. — Residential &amp; Commercial HVAC</title>
<link href="https://fonts.googleapis.com/css2?family=Montserrat:wght@400;500;600;700;800&family=Open+Sans:wght@400;600&family=Great+Vibes&display=swap" rel="stylesheet">
<style>
:root{
  --red:#e0524b;
  --red-deep:#c93c36;
  --red-soft:#ec6f68;
  --ink:#23252b;
  --text:#5d6068;
  --muted:#9a9ca3;
  --line:#e6e6ea;
  --paper:#ffffff;
  --mist:#f4f4f6;
  --night:#26272d;
  --night-2:#1d1e23;
}
*{box-sizing:border-box;margin:0;padding:0}
html,body{width:1200px;height:4920px;overflow:hidden}
body{font-family:"Open Sans",sans-serif;color:var(--text);background:var(--paper);position:relative;font-size:13px;line-height:1.6}
h1,h2,h3,h4,.btn,.nav a{font-family:"Montserrat",sans-serif}
.section{position:absolute;left:0;width:1200px}
.btn{display:inline-block;background:var(--red);color:#fff;font-size:10px;font-weight:700;letter-spacing:.6px;text-transform:uppercase;padding:9px 18px;border-radius:3px}
.btn-ghost{background:transparent;border:1px solid #fff}
.script{font-family:"Great Vibes",cursive;font-size:30px;line-height:1}
.eyebrow{font-family:"Montserrat",sans-serif;font-size:11px;font-weight:700;letter-spacing:1.5px;text-transform:uppercase}
.photo{position:absolute}

/* header */
.site-header{position:absolute;top:0;left:0;width:1200px;height:86px;z-index:5;display:flex;align-items:center;padding:0 60px}
.brand{display:flex;align-items:center;gap:10px;color:#fff;font-family:"Montserrat",sans-serif;font-weight:800;font-size:26px;letter-spacing:1px}
.brand-square{width:16px;height:16px;background:var(--red)}
.nav{display:flex;gap:18px;margin-left:70px;margin-top:22px}
.nav a{color:#fff;font-size:11px;font-weight:500;text-decoration:none;white-space:nowrap}
.header-call{position:absolute;right:190px;top:14px;color:#fff;display:flex;gap:8px;align-items:center;font-size:10px;line-height:1.3}
.header-call b{font-family:"Montserrat",sans-serif;font-size:13px}
.header-cta{position:absolute;right:50px;top:16px}
.header-cta .btn{background:#f08c2a}

/* hero */
.hero{top:0;height:600px;background:linear-gradient(180deg,#2b2124 0%,#5b2c2b 55%,#8a3a36 100%);overflow:hidden}
.hero-copy{position:absolute;left:220px;top:190px;color:#fff}
.hero-copy .lead{font-family:"Montserrat",sans-serif;font-size:32px;font-weight:500;line-height:1.05}
.hero-copy h1{font-size:46px;font-weight:800;color:var(--red-soft);line-height:1.15;letter-spacing:.5px;white-space:nowrap}
.hero-copy p{font-family:"Montserrat",sans-serif;font-size:17px;font-weight:600;margin:10px 0 18px}
.hero-copy .btn{margin-right:10px}
.hero-arrow{position:absolute;top:290px;width:26px;height:26px;border-radius:50%;background:#fff;display:flex;align-items:center;justify-content:center}
.consult{position:absolute;left:700px;top:340px;width:254px;height:248px;background:linear-gradient(160deg,var(--red-deep),var(--red));padding:18px 22px;z-index:4;box-shadow:0 10px 30px rgba(0,0,0,.25)}
.consult h3{color:#fff;font-size:13px;font-weight:700;letter-spacing:.5px;margin-bottom:10px}
.field{background:#fff;height:24px;margin-bottom:7px;font-size:10px;color:var(--muted);padding:4px 8px}
.field.area{height:50px}
.consult .btn{background:#fff;color:var(--red);margin-top:4px}

/* about */
.about{top:600px;height:540px}
.about-copy{position:absolute;left:220px;top:140px;width:320px}
.about-copy h2{font-size:26px;font-weight:700;color:var(--ink);line-height:1.25;margin-bottom:12px}
.about-copy p{font-size:11px;margin-bottom:10px}
.about-copy .btn{background:#fff;color:var(--red);border:1px solid var(--red)}
.about-shadow{position:absolute;left:620px;top:60px;width:380px;height:380px;background:var(--red)}
.about-photo{left:600px;top:40px;width:380px;height:360px;background:linear-gradient(160deg,#e9ecef,#b9c0c7)}

/* services */
.services{top:1140px;height:740px;background:linear-gradient(135deg,var(--red-soft) 0%,var(--red) 50%,var(--red-deep) 100%)}
.section-title{text-align:center;color:#fff}
.section-title h2{font-size:30px;font-weight:700;margin-top:2px}
.service-card{position:absolute;width:420px;height:220px;background:#fff;display:flex;box-shadow:0 8px 22px rgba(0,0,0,.15)}
.service-card .photo{position:relative;width:190px;height:220px;flex:none}
.service-body{padding:34px 22px}
.service-body h3{font-size:13px;font-weight:700;color:var(--ink);text-transform:uppercase;margin-bottom:10px}
.service-body p{font-size:11px;margin-bottom:18px}

/* solutions */
.solutions{top:1880px;height:560px;text-align:center}
.solutions .eyebrow{color:var(--ink);margin-top:70px}
.solutions h2{font-size:30px;font-weight:700;color:var(--ink);margin-top:4px}
.solutions h2 span{color:var(--red)}
.solutions .sub{font-size:12px;font-family:"Montserrat",sans-serif;color:var(--ink)}
.sol-grid{position:absolute;left:300px;top:170px;width:780px;display:grid;grid-template-columns:repeat(3,1fr);row-gap:40px;text-align:left}
.sol-item{display:flex;gap:10px}
.sol-icon{width:26px;height:26px;flex:none}
.sol-item h4{font-size:11px;font-weight:700;color:var(--ink);line-height:1.3;margin-bottom:4px}
.sol-item p{font-size:10px;line-height:1.45;width:170px}
.sol-bar{position:absolute;left:240px;top:400px;width:720px;height:60px;border-top:1px solid var(--line);border-bottom:1px solid var(--line);display:flex;align-items:center;justify-content:space-between;text-align:left;padding:0 20px}
.sol-bar p{font-size:11px;width:400px;color:var(--ink);line-height:1.4}
.sol-note{position:absolute;left:260px;top:470px;font-size:10px;color:var(--red)}

/* experience */
.experience{top:2440px;height:380px;background:linear-gradient(120deg,#fafafb 0%,#f1f1f3 60%,#ffffff 100%)}
.experience h2{position:absolute;left:230px;top:130px;font-size:28px;font-weight:600;color:var(--ink);line-height:1.25}
.experience h2 span{color:var(--red)}
.exp-photo{left:600px;top:20px;width:380px;height:300px;background:linear-gradient(150deg,#d7cbb9,#7d8a96)}

/* savings */
.savings{top:2820px;height:700px;background:var(--mist)}
.savings-photo{left:0;top:160px;width:1200px;height:540px;background:linear-gradient(180deg,#d9d2c9 0%,#bdaf9f 55%,#8e7d6c 100%)}
.savings h2{position:absolute;top:120px;width:100%;text-align:center;font-size:24px;font-weight:700;color:var(--ink);letter-spacing:1px}
.save-cards{position:absolute;left:192px;top:200px;display:flex;gap:20px}
.save-card{width:256px;height:180px;background:#fff;padding:16px 18px;box-shadow:0 6px 18px rgba(0,0,0,.12)}
.save-card h3{font-size:17px;font-weight:700;color:var(--ink);margin:8px 0 4px}
.save-card p{font-size:10px;line-height:1.45;margin-bottom:8px}
.save-card a{font-family:"Montserrat",sans-serif;font-size:9px;font-weight:700;color:var(--red);text-decoration:none;text-transform:uppercase}

/* testimonials */
.testimonials{top:3520px;height:560px;background:linear-gradient(135deg,var(--red-soft),var(--red) 60%,var(--red-deep))}
.testimonials .section-title{padding-top:74px}
.testimonials .eyebrow{color:#fff}
.quote-card{position:absolute;top:210px;width:310px;height:250px;background:#fff;text-align:center;padding:20px 26px}
.avatar{width:44px;height:44px;border-radius:50%;background:linear-gradient(135deg,#ccc,#999);margin:0 auto 6px}
.quote-card h4{font-size:13px;font-weight:700;color:var(--ink)}
.quote-card small{font-size:9px;color:var(--muted)}
.quote-card p{font-size:10px;line-height:1.6;margin-top:10px}
.stars{color:#f2b33d;font-size:12px;margin-top:8px}
.testimonials .more{position:absolute;left:0;width:100%;top:480px;text-align:center}
.testimonials .more .btn{background:#fff;color:var(--red)}

/* call to action */
.cta{top:4080px;height:320px}
.cta h2{position:absolute;left:240px;top:70px;width:560px;font-size:23px;font-weight:500;color:var(--ink);line-height:1.35}
.cta h2 span{color:var(--red);font-weight:700}
.cta .note{position:absolute;left:240px;top:170px;font-size:11px}
.cta-phone{position:absolute;left:300px;top:220px;display:flex;align-items:center;gap:10px;line-height:1.2}
.cta-phone small{font-size:9px;color:var(--muted);display:block}
.cta-phone b{font-family:"Montserrat",sans-serif;font-size:20px;color:var(--ink)}
.phone-dot{width:32px;height:32px;border-radius:50%;background:var(--red);display:flex;align-items:center;justify-content:center}
.cta .request{position:absolute;left:660px;top:226px}
.van{left:820px;top:180px;width:380px;height:180px;background:linear-gradient(180deg,#f7f7f8,#d6d8dc);border-radius:30px 60px 10px 10px;z-index:3}

/* footer */
.footer{top:4400px;height:520px;background:var(--night);color:#b9bac0}
.foot-contacts{position:absolute;left:240px;top:70px;width:720px;display:flex;justify-content:space-between}
.foot-contact{display:flex;gap:10px;font-size:10px;line-height:1.4;width:210px}
.foot-contact .dot{width:30px;height:30px;border-radius:50%;border:1px solid var(--red);flex:none;display:flex;align-items:center;justify-content:center}
.foot-contact b{color:#fff;font-family:"Montserrat",sans-serif;font-size:11px;display:block}
.foot-brand{position:absolute;left:240px;top:220px;width:200px}
.foot-brand .brand{font-size:24px;margin-bottom:10px}
.foot-brand p{font-size:10px;line-height:1.5}
.foot-col{position:absolute;top:210px}
.foot-col h4{color:#fff;font-size:11px;font-weight:700;margin-bottom:10px}
.foot-col li{list-style:none;font-size:10px;line-height:1.9}
.socials{position:absolute;left:850px;top:370px;display:flex;gap:6px;align-items:center}
.socials span.lbl{font-family:"Montserrat",sans-serif;font-size:10px;color:#fff;margin-right:6px;font-weight:700}
.socials i{width:20px;height:20px;border-radius:50%;background:var(--red);display:block}
.foot-bottom{position:absolute;left:0;bottom:0;width:1200px;height:50px;background:var(--night-2);display:flex;align-items:center;justify-content:space-between;padding:0 240px;font-size:9px}
</style>
</head>
<body>

<header class="site-header">
  <div class="brand"><span class="brand-square"></span>VELMOR</div>
  <nav class="nav">
    <a>Home</a><a>Residential</a><a>Commercial</a><a>Testimonials</a><a>Gallery</a><a>About Us</a><a>Coupons</a><a>Contact Us</a>
  </nav>
  <div class="header-call">
    <svg width="16" height="16" viewBox="0 0 24 24" fill="#fff"><path d="M6.6 10.8a15 15 0 0 0 6.6 6.6l2.2-2.2a1 1 0 0 1 1-.25 11.4 11.4 0 0 0 3.6.57 1 1 0 0 1 1 1V20a1 1 0 0 1-1 1A17 17 0 0 1 3 4a1 1 0 0 1 1-1h3.5a1 1 0 0 1 1 1c0 1.25.2 2.45.57 3.57a1 1 0 0 1-.25 1z"/></svg>
    <div>Call us<br><b>718 555-0142</b></div>
  </div>
  <div class="header-cta"><span class="btn">Request Service</span></div>
</header>

<section class="section hero">
  <div class="photo" role="img" aria-label="City skyline at dusk behind the hero message" style="inset:0;background:linear-gradient(180deg,rgba(40,30,34,.35),rgba(201,60,54,.35))"></div>
  <div class="hero-arrow" style="left:44px"><svg width="10" height="10" viewBox="0 0 10 10"><path d="M6.5 1.5 3 5l3.5 3.5" stroke="#333" stroke-width="1.6" fill="none"/></svg></div>
  <div class="hero-arrow" style="right:44px"><svg width="10" height="10" viewBox="0 0 10 10"><path d="M3.5 1.5 7 5 3.5 8.5" stroke="#333" stroke-width="1.6" fill="none"/></svg></div>
  <div class="hero-copy">
    <div class="lead">YOUR COMFORT IS</div>
    <h1>JUST A CALL AWAY</h1>
    <p>Residential &amp; Commercial HVAC Solutions!</p>
    <span class="btn">Heating Service</span><span class="btn btn-ghost">Cooling Service</span>
  </div>
  <form class="consult">
    <h3>FREE CONSULTATION</h3>
    <div class="field">Name*</div>
    <div class="field">Phone*</div>
    <div class="field">Email*</div>
    <div class="field area">Message</div>
    <span class="btn">Send Message</span>
  </form>
</section>

<section class="section about">
  <div class="about-copy">
    <h2>Local Brooklyn,<br>NY HVAC Contractors</h2>
    <p>Velmor Mechanical Air Duct Installation, Furnace, Air Conditioning repair and replacement company offers top repair services.</p>
    <p>We can service any brand that may show a little wear and tear. Our Brooklyn HVAC heating, ventilating, and air conditioning technicians are experts at inspecting and repairing systems before a small issue becomes a costly repair.</p>
    <span class="btn">Learn More</span>
  </div>
  <div class="about-shadow"></div>
  <div class="photo about-photo" role="img" aria-label="Outdoor central air conditioning condenser unit"></div>
</section>

<section class="section services">
  <div class="section-title" style="padding-top:96px">
    <div class="script">Our Services</div>
    <h2>Heating and Cooling Solutions</h2>
  </div>
  <div class="service-card" style="left:160px;top:200px">
    <div class="photo" role="img" aria-label="Person relaxing near a wall air conditioner" style="background:linear-gradient(150deg,#dfe3e6,#9aa6ae)"></div>
    <div class="service-body"><h3>Air Conditioning</h3><p>Experience consistently quality comfortable air conditioning service.</p><span class="btn">Request Service</span></div>
  </div>
  <div class="service-card" style="left:620px;top:200px">
    <div class="photo" role="img" aria-label="Technician servicing an air conditioning unit" style="background:linear-gradient(150deg,#e4e0db,#9b9389)"></div>
    <div class="service-body"><h3>Air Conditioning</h3><p>Experience consistently quality comfortable air conditioning service.</p><span class="btn">Request Service</span></div>
  </div>
  <div class="service-card" style="left:160px;top:460px">
    <div class="photo" role="img" aria-label="Technician repairing an indoor unit" style="background:linear-gradient(150deg,#e6e8ea,#a4adb5)"></div>
    <div class="service-body"><h3>Repairs</h3><p>Experience consistently quality comfortable air conditioning service.</p><span class="btn">Request Service</span></div>
  </div>
  <div class="service-card" style="left:620px;top:460px">
    <div class="photo" role="img" aria-label="Pressure gauges used for refrigerant service" style="background:linear-gradient(150deg,#c6d1d8,#b04a45)"></div>
    <div class="service-body"><h3>Serving Your Area</h3><p>Experience consistently quality comfortable air conditioning service.</p><span class="btn">Request Service</span></div>
  </div>
</section>

<section class="section solutions">
  <div class="eyebrow">Solutions</div>
  <h2>Trusted Home &amp; Commercial <span>Solutions.</span></h2>
  <div class="sub">Serving both Residential &amp; Commercial Heating &amp; Air Conditioning Needs</div>
  <div class="sol-grid">
    <div class="sol-item"><svg class="sol-icon" viewBox="0 0 26 26"><circle cx="13" cy="13" r="11" fill="none" stroke="#e0524b" stroke-width="2"/><path d="M8 13h10M13 8v10" stroke="#e0524b" stroke-width="2"/></svg><div><h4>Air Purifier System</h4><p>Lorem Ipsum is simply dummy text of the printing.</p></div></div>
    <div class="sol-item"><svg class="sol-icon" viewBox="0 0 26 26"><rect x="3" y="5" width="20" height="16" rx="2" fill="none" stroke="#e0524b" stroke-width="2"/><path d="M7 15l4-4 3 3 5-5" stroke="#e0524b" stroke-width="2" fill="none"/></svg><div><h4>HVAC Maintenance<br>Tune Up and Inspection</h4><p>Lorem Ipsum is simply dummy text of the printing.</p></div></div>
    <div class="sol-item"><svg class="sol-icon" viewBox="0 0 26 26"><path d="M5 21 15 11M14 6a5 5 0 0 0 6 6l-3-3z" stroke="#e0524b" stroke-width="2" fill="none"/></svg><div><h4>HVAC Parts, Repair,<br>Installation</h4><p>Lorem Ipsum is simply dummy text of the printing.</p></div></div>
    <div class="sol-item"><svg class="sol-icon" viewBox="0 0 26 26"><rect x="4" y="4" width="18" height="18" rx="2" fill="none" stroke="#e0524b" stroke-width="2"/><path d="M8 10h10M8 14h10M8 18h6" stroke="#e0524b" stroke-width="2"/></svg><div><h4>HVAC Replacement<br>Cool and Installation</h4><p>Lorem Ipsum is simply dummy text of the printing.</p></div></div>
    <div class="sol-item"><svg class="sol-icon" viewBox="0 0 26 26"><path d="M3 9h20M3 17h20M8 5v16M18 5v16" stroke="#e0524b" stroke-width="2"/></svg><div><h4>Ductless Systems</h4><p>Lorem Ipsum is simply dummy text of the printing.</p></div></div>
    <div class="sol-item"><svg class="sol-icon" viewBox="0 0 26 26"><path d="M13 3c4 5 6 8 6 12a6 6 0 0 1-12 0c0-4 2-7 6-12z" fill="none" stroke="#e0524b" stroke-width="2"/></svg><div><h4>Gas Furnace Installations</h4><p>Lorem Ipsum is simply dummy text of the printing.</p></div></div>
  </div>
  <div class="sol-bar">
    <p>Velmor Mechanical Contractors Corp is Here To Assist You With All Professional HVAC Services</p>
    <span class="btn">Get Started Now</span>
  </div>
  <div class="sol-note">Please Call To Confirm Service In Your Area</div>
</section>

<section class="section experience">
  <h2>We're Backed<br>by 20 Years of<br><span>Experience.</span></h2>
  <div class="photo exp-photo" role="img" aria-label="Technician's gloved hands working on refrigerant lines"></div>
</section>

<section class="section savings">
  <div class="photo savings-photo" role="img" aria-label="Happy family relaxing together on a sofa at home"></div>
  <h2>SAVINGS CENTER</h2>
  <div class="save-cards">
    <div class="save-card">
      <svg width="30" height="30" viewBox="0 0 30 30"><rect x="5" y="4" width="20" height="23" rx="2" fill="none" stroke="#23252b" stroke-width="2"/><path d="M10 11h10M10 16h10M10 21h6" stroke="#e0524b" stroke-width="2"/></svg>
      <h3>Maint Plan</h3>
      <p>Lorem ipsum dolor sit amet consectetur adipiscing elit. We care about keeping your system running well every season.</p>
      <a>Maintenance Plans →</a>
    </div>
    <div class="save-card">
      <svg width="30" height="30" viewBox="0 0 30 30"><rect x="3" y="7" width="24" height="16" rx="2" fill="none" stroke="#23252b" stroke-width="2"/><path d="M3 12h24" stroke="#e0524b" stroke-width="3"/></svg>
      <h3>Financing</h3>
      <p>Lorem ipsum dolor sit amet consectetur adipiscing elit. Simple payment options for new systems and major repairs.</p>
      <a>Apply For Financing →</a>
    </div>
    <div class="save-card">
      <svg width="30" height="30" viewBox="0 0 30 30"><path d="M4 15 15 4h10v10L14 25z" fill="none" stroke="#23252b" stroke-width="2"/><circle cx="20" cy="9" r="2" fill="#e0524b"/></svg>
      <h3>Promotions</h3>
      <p>Lorem ipsum dolor sit amet consectetur adipiscing elit. Check current coupons and seasonal deals on service.</p>
      <a>View All Coupons →</a>
    </div>
  </div>
</section>

<section class="section testimonials">
  <div class="section-title">
    <div class="eyebrow">Testimonials</div>
    <h2>Our Happy Customers Say</h2>
  </div>
  <div class="quote-card" style="left:278px">
    <div class="avatar" role="img" aria-label="Customer portrait"></div>
    <h4>Richard C.</h4><small>CEO &amp; Founder</small>
    <p>Thank you so much for doing such a wonderful job on our air conditioning unit. I am very happy with the service provided by Velmor Mechanical Contractors. The staff gathers its information before helping me out and did their very best for me. I am thankful for all of your help and service.</p>
    <div class="stars">★★★★★</div>
  </div>
  <div class="quote-card" style="left:612px">
    <div class="avatar" role="img" aria-label="Customer portrait"></div>
    <h4>Richard C.</h4><small>CEO &amp; Founder</small>
    <p>Thank you so much for doing such a wonderful job on our air conditioning unit. I am very happy with the service provided by Velmor Mechanical Contractors. The staff gathers its information before helping me out and did their very best for me. I am thankful for all of your help and service.</p>
    <div class="stars">★★★★★</div>
  </div>
  <div class="more"><span class="btn">Click Here</span></div>
</section>

<section class="section cta">
  <h2>To schedule an appointment with our furnace and <span>air conditioning repair and installation experts.</span></h2>
  <div class="note">We will be in touch with you to verify your appointment.</div>
  <div class="cta-phone">
    <span class="phone-dot"><svg width="14" height="14" viewBox="0 0 24 24" fill="#fff"><path d="M6.6 10.8a15 15 0 0 0 6.6 6.6l2.2-2.2a1 1 0 0 1 1-.25 11.4 11.4 0 0 0 3.6.57 1 1 0 0 1 1 1V20a1 1 0 0 1-1 1A17 17 0 0 1 3 4a1 1 0 0 1 1-1h3.5a1 1 0 0 1 1 1c0 1.25.2 2.45.57 3.57a1 1 0 0 1-.25 1z"/></svg></span>
    <div><small>NEED HELP NOW?</small><b>Call: 718 555-0142</b></div>
  </div>
  <span class="btn request">Request Service</span>
  <div class="photo van" role="img" aria-label="White company service van"></div>
</section>

<footer class="section footer">
  <div class="foot-contacts">
    <div class="foot-contact"><span class="dot"><svg width="12" height="12" viewBox="0 0 24 24" fill="#e0524b"><path d="M12 2a7 7 0 0 0-7 7c0 5 7 13 7 13s7-8 7-13a7 7 0 0 0-7-7zm0 9.5A2.5 2.5 0 1 1 12 6.5a2.5 2.5 0 0 1 0 5z"/></svg></span><div>Velmor Corp. is a full service mechanical contractor serving Brooklyn, NY</div></div>
    <div class="foot-contact"><span class="dot"><svg width="12" height="12" viewBox="0 0 24 24" fill="#e0524b"><path d="M6.6 10.8a15 15 0 0 0 6.6 6.6l2.2-2.2a1 1 0 0 1 1-.25 11.4 11.4 0 0 0 3.6.57 1 1 0 0 1 1 1V20a1 1 0 0 1-1 1A17 17 0 0 1 3 4a1 1 0 0 1 1-1h3.5a1 1 0 0 1 1 1c0 1.25.2 2.45.57 3.57a1 1 0 0 1-.25 1z"/></svg></span><div><b>Phone</b>718 555-0142</div></div>
    <div class="foot-contact"><span class="dot"><svg width="12" height="12" viewBox="0 0 24 24"><rect x="3" y="6" width="18" height="12" rx="1" fill="none" stroke="#e0524b" stroke-width="2"/><path d="m3 7 9 6 9-6" stroke="#e0524b" stroke-width="2" fill="none"/></svg></span><div><b>Email</b>info@velmorcorp.example</div></div>
  </div>
  <div class="foot-brand">
    <div class="brand"><span class="brand-square"></span>VELMOR</div>
    <p>Lorem ipsum is simply dummy text of the printing and typesetting industry. Lorem ipsum has been the standard.</p>
  </div>
  <div class="foot-col" style="left:540px"><h4>LINKS</h4><ul><li>Home</li><li>Residential</li><li>Commercial</li><li>Testimonials</li><li>Gallery</li><li>About Us</li><li>Coupons</li></ul></div>
  <div class="foot-col" style="left:690px"><h4>AIR CONDITIONING</h4><ul><li>AC Repair</li><li>AC Installation</li><li>AC Maintenance</li><li>Ductless AC Systems</li></ul></div>
  <div class="foot-col" style="left:860px"><h4>HEATING</h4><ul><li>Furnace Repair</li><li>Furnace Installation</li><li>Furnace Service</li><li>Gas Furnaces</li></ul></div>
  <div class="socials"><span class="lbl">Follow</span><i></i><i></i><i></i><i></i><i></i></div>
  <div class="foot-bottom"><span>© 2024 Velmor Corp. All Rights Reserved.</span><span>Privacy Policy &nbsp;|&nbsp; Terms of Use</span></div>
</footer>

</body>
</html>
```